Carver Lindqvist Group Business Cards

We have a new logo, and want to design new business cards with it. We are 21 years in business, and want a fresh but professional look, so not a lot of extra stuff on the card. We are a recruiting and staffing firm focused on placing accounting and finance professionals in the Dallas TX area. I've attached our new logo that should be displayed on the cards. Here is what I think we want on the cards:
Ray Pemberly, CPA
Partner and Managing Director
8282 Orchard Vale Rd.
Suite 610
Dallas, TX 75391
O 214-555-0184
M 214-555-0237
ray@carverlindqvist.example
www.carverlindqvist.example

```html
<!DOCTYPE html>
<html lang="en">
<head>
<meta charset="utf-8">
<title>Carver Lindqvist Group – Business Cards</title>
<link rel="stylesheet" href="https://fonts.googleapis.com/css2?family=Montserrat:wght@400;700;800&family=Lato:wght@400&display=swap">
<style>
  :root {
    --brand-blue: #0b3a9e;
    --brand-blue-light: #4f6fbf;
    --ink-gray: #444a55;
    --card-white: #ffffff;
    --backdrop: #e9e6e1;
    --card-shadow: rgba(0, 0, 0, 0.22);
  }
  * { box-sizing: border-box; margin: 0; padding: 0; }
  html, body { width: 1200px; height: 900px; overflow: hidden; }
  body { background: var(--backdrop); position: relative; font-family: "Lato", sans-serif; }

  .card {
    position: absolute;
    width: 620px;
    height: 354px;
    box-shadow: 0 10px 28px var(--card-shadow);
    overflow: hidden;
  }

  /* Back of card */
  .card-back {
    left: 70px;
    top: 90px;
    background: var(--brand-blue);
    display: flex;
    align-items: center;
    justify-content: center;
  }
  .card-back .brand-name {
    color: var(--card-white);
    font-family: "Montserrat", sans-serif;
    font-weight: 800;
    font-size: 44px;
    line-height: 1.1;
    text-align: center;
    letter-spacing: 0.5px;
  }

  /* Front of card */
  .card-front {
    left: 510px;
    top: 440px;
    background: var(--card-white);
  }
  .wave { position: absolute; left: 0; top: 0; width: 620px; height: 354px; }

  .identity { position: absolute; left: 48px; top: 50px; }
  .person-name {
    font-family: "Montserrat", sans-serif;
    font-weight: 700;
    font-size: 22px;
    color: var(--brand-blue);
    letter-spacing: 0.3px;
  }
  .person-name .credential { font-weight: 400; font-size: 17px; }
  .person-title {
    font-family: "Montserrat", sans-serif;
    font-size: 14px;
    color: var(--ink-gray);
    margin-top: 2px;
  }

  .brand-lockup {
    position: absolute;
    right: 40px;
    top: 44px;
    font-family: "Montserrat", sans-serif;
    font-weight: 700;
    font-size: 24px;
    line-height: 1.15;
    color: var(--brand-blue);
    text-align: right;
  }

  .contact { position: absolute; left: 48px; top: 168px; font-size: 16px; color: var(--ink-gray); }
  .contact-line { display: flex; align-items: center; gap: 8px; height: 22px; }
  .contact-line svg { width: 14px; height: 14px; fill: var(--brand-blue); flex: none; }
  .address { margin-top: 6px; line-height: 22px; }

  .website {
    position: absolute;
    right: 32px;
    bottom: 30px;
    color: var(--card-white);
    font-size: 15px;
    letter-spacing: 0.3px;
  }
</style>
</head>
<body>
  <section class="card card-back" aria-label="Card back">
    <p class="brand-name">Carver Lindqvist<br>Group</p>
  </section>

  <section class="card card-front" aria-label="Card front">
    <svg class="wave" viewBox="0 0 620 354" aria-hidden="true">
      <path d="M0,300 C140,345 330,320 470,250 C540,215 585,185 620,168 L620,354 L0,354 Z" fill="var(--brand-blue-light)"/>
      <path d="M0,318 C150,350 340,330 480,262 C545,230 590,200 620,182 L620,354 L0,354 Z" fill="var(--card-white)"/>
      <path d="M0,326 C150,356 350,338 490,270 C550,240 595,210 620,192 L620,354 L0,354 Z" fill="var(--brand-blue)"/>
    </svg>

    <div class="identity">
      <h1 class="person-name">RAY PEMBERLY<span class="credential">, CPA</span></h1>
      <p class="person-title">Partner and Managing Director</p>
    </div>

    <p class="brand-lockup">Carver Lindqvist<br>Group</p>

    <div class="contact">
      <p class="contact-line">
        <svg viewBox="0 0 16 16" aria-label="Office"><path d="M3 6c0-2 2-3 5-3s5 1 5 3l-2 1-1-2H6L5 7 3 6zm2 2h6l2 5H3l2-5zm3 1a1.5 1.5 0 100 3 1.5 1.5 0 000-3z"/></svg>
        214-555-0184
      </p>
      <p class="contact-line">
        <svg viewBox="0 0 16 16" aria-label="Mobile"><path d="M5 1h6a1 1 0 011 1v12a1 1 0 01-1 1H5a1 1 0 01-1-1V2a1 1 0 011-1zm1 2v9h4V3H6zm2 10a.8.8 0 100 1.6.8.8 0 000-1.6z"/></svg>
        214-555-0237
      </p>
      <p class="contact-line">
        <svg viewBox="0 0 16 16" aria-label="Email"><path d="M1 3h14v10H1V3zm1.5 1.2L8 8.5l5.5-4.3H2.5z"/></svg>
        ray@carverlindqvist.example
      </p>
      <p class="address">8282 Orchard Vale Rd.<br>Suite 610 Dallas, TX 75391</p>
    </div>

    <p class="website">www.carverlindqvist.example</p>
  </section>
</body>
</html>
```